Yacht, Boats, Watersports company needs a redesign of business card

Hello Designers!
We are a Boat dealership company that sells fun in the water, we sell boats, Yachts, Kayaks and also yacht WaterSport toys. We are looking to redesign our business cards in to something a little bit more sophisticated. in a way that we can make better use of our company colors. I'm attaching a zipped file containing the company 3 sets of company logo which one is an horizontal another one is a vertical and also a chromed 3d logo. Also is included two set of business cards that we use and also some designs that i think it's interesting. We use PMS 2026c Orange and PMS 7687C Blue. I would like to see at least two different options with the orange as accent and also using blue as an accent color. It's really important for the business cards to have a font option and size that is legible to most people. Our current website is wwww.corvellamarine.com. Please visit if you want to have a better feeling of the Boat dealership
You can send Single sided or double side options. We are now using single sided but we may be open for a double side option if we really like the design.
Target Market(s)
Marine, boat sales, yacht sales, water toys sales/
Contact Information for Business Card
Name: Dale Pritchett
Address: 718 West Halden Lane,
Marlow Harbor, FL 33019
Phone: 954-382-7146
Fax: 954:382-7139
Cell: 954-451-8320
Email: 212@corvellamarine.com
Website: corvellamarine.com
Requirements
Must have
- the current information of the business card provided.
logo
use the PMS Colors
Nice to have
- a touch of elegance and sophistication but simple
Should not have
- should not have any typography that is hard to read, the card should be simple but yet sophisticated.

```html
<!DOCTYPE html>
<html lang="en">
<head>
<meta charset="utf-8">
<title>Corvella Marine – Business Card Options</title>
<link rel="stylesheet" href="https://fonts.googleapis.com/css2?family=Montserrat:wght@700&family=Roboto+Condensed:wght@400;700&display=swap">
<style>
  :root {
    --brand-orange: #ee7125;
    --brand-blue: #1656a3;
    --bleed-grey: #b3b3b3;
    --card-white: #ffffff;
    --ink: #222222;
  }
  html, body {
    margin: 0;
    padding: 0;
    width: 1200px;
    height: 1200px;
    overflow: hidden;
    background: var(--card-white);
  }
  .board { display: block; width: 1200px; height: 1200px; }
  .bleed-area { fill: var(--bleed-grey); }
  .bleed-label { font-family: Arial, "Roboto Condensed", sans-serif; font-size: 5px; fill: var(--ink); }
  .wordmark { font-family: "Montserrat", sans-serif; font-weight: 700; font-size: 12.5px; fill: var(--brand-blue); letter-spacing: 0.2px; }
  .web-address { font-family: "Roboto Condensed", sans-serif; font-size: 6.6px; fill: var(--card-white); letter-spacing: 1.4px; }
  .holder-name { font-family: "Roboto Condensed", sans-serif; font-weight: 700; font-size: 10px; }
  .holder-title { font-family: "Roboto Condensed", sans-serif; font-weight: 700; font-size: 6px; fill: var(--card-white); letter-spacing: 0.3px; }
  .contact-line { font-family: "Roboto Condensed", sans-serif; font-size: 6.2px; fill: var(--card-white); }
  .on-orange .holder-name { fill: var(--brand-blue); }
  .on-blue .holder-name { fill: var(--brand-orange); }
  .contact-icon { color: var(--brand-orange); }
  .social-square { fill: var(--brand-blue); }
  .on-blue .social-square { fill: var(--brand-orange); }
</style>
</head>
<body>
<svg class="board" viewBox="0 0 576 576" xmlns="http://www.w3.org/2000/svg" aria-label="Four business card layouts for Corvella Marine">
  <defs>
    <clipPath id="card-shape"><rect x="0" y="0" width="252" height="147" rx="16"/></clipPath>
    <g id="icon-phone">
      <circle r="5.5" fill="#ffffff"/>
      <rect x="-3" y="-1" width="6" height="3" rx="0.8" fill="currentColor"/>
      <path d="M-3.2 -1.2 Q0 -3.6 3.2 -1.2" fill="none" stroke="currentColor" stroke-width="1.2"/>
    </g>
    <g id="icon-fax">
      <circle r="5.5" fill="#ffffff"/>
      <rect x="-3" y="-1.5" width="6" height="3.5" rx="0.6" fill="currentColor"/>
      <rect x="-1.8" y="-3.3" width="3.6" height="1.6" fill="currentColor"/>
    </g>
    <g id="icon-home">
      <circle r="5.5" fill="#ffffff"/>
      <path d="M0 -3.4 L3.4 -0.4 H2.3 V3 H-2.3 V-0.4 H-3.4 Z" fill="currentColor"/>
    </g>
    <g id="icon-mail">
      <circle r="5.5" fill="#ffffff"/>
      <rect x="-3.2" y="-2.2" width="6.4" height="4.4" rx="0.5" fill="none" stroke="currentColor" stroke-width="1"/>
      <path d="M-3.2 -2 L0 0.6 L3.2 -2" fill="none" stroke="currentColor" stroke-width="0.9"/>
    </g>
  </defs>

  <!-- Front, option A -->
  <g class="card-front" transform="translate(10 113)">
    <rect class="bleed-area" width="273" height="162"/>
    <g transform="translate(9 8)">
      <g clip-path="url(#card-shape)">
        <rect width="252" height="147" fill="var(--card-white)"/>
        <rect y="100" width="252" height="22" fill="var(--brand-orange)"/>
        <rect y="122" width="252" height="25" fill="var(--brand-blue)"/>
      </g>
      <circle cx="126" cy="37" r="18" fill="none" stroke="var(--brand-blue)" stroke-width="3.5"/>
      <text class="wordmark" x="126" y="84" text-anchor="middle">CORVELLA MARINE</text>
      <text class="web-address" x="126" y="137" text-anchor="middle">www.corvellamarine.com</text>
    </g>
    <text class="bleed-label" transform="translate(7 81) rotate(-90)" text-anchor="middle">bleed</text>
    <text class="bleed-label" x="110" y="160">bleed</text>
  </g>

  <!-- Front, option B -->
  <g class="card-front" transform="translate(293 113)">
    <rect class="bleed-area" width="273" height="162"/>
    <g transform="translate(9 8)">
      <g clip-path="url(#card-shape)">
        <rect width="252" height="147" fill="var(--card-white)"/>
        <rect y="96" width="252" height="21" fill="var(--brand-orange)"/>
        <rect y="122" width="252" height="25" fill="var(--brand-blue)"/>
      </g>
      <circle cx="126" cy="37" r="18" fill="none" stroke="var(--brand-blue)" stroke-width="3.5"/>
      <text class="wordmark" x="126" y="84" text-anchor="middle">CORVELLA MARINE</text>
    </g>
    <text class="bleed-label" transform="translate(6 81) rotate(-90)" text-anchor="middle">bleed</text>
    <text class="bleed-label" x="95" y="160">bleed</text>
  </g>

  <!-- Back, orange field -->
  <g class="card-back on-orange" transform="translate(10 295)">
    <rect class="bleed-area" width="273" height="163"/>
    <g transform="translate(9 9)">
      <g clip-path="url(#card-shape)">
        <rect width="252" height="147" fill="var(--brand-orange)"/>
        <rect y="123" width="252" height="24" fill="var(--brand-blue)"/>
      </g>
      <text class="holder-name" x="4" y="23">DALE PRITCHETT</text>
      <text class="holder-title" x="4" y="32">CORPORATE MANAGER</text>
      <use class="contact-icon" href="#icon-phone" x="126" y="40"/>
      <text class="contact-line" x="136" y="39">1.954.382.7146</text>
      <text class="contact-line" x="136" y="46">1.954.451.8320</text>
      <use class="contact-icon" href="#icon-fax" x="126" y="61"/>
      <text class="contact-line" x="136" y="63">1.954.382.7139</text>
      <use class="contact-icon" href="#icon-home" x="126" y="79"/>
      <text class="contact-line" x="136" y="78">718 West Halden Lane</text>
      <text class="contact-line" x="136" y="86">Marlow Harbor, FL 33019</text>
      <use class="contact-icon" href="#icon-mail" x="126" y="99"/>
      <text class="contact-line" x="136" y="101">212@corvellamarine.com</text>
      <rect class="social-square" x="4" y="94" width="10" height="10" rx="1"/>
      <rect class="social-square" x="19" y="94" width="10" height="10" rx="1"/>
      <rect class="social-square" x="34" y="94" width="10" height="10" rx="1"/>
      <text class="web-address" x="126" y="138" text-anchor="middle">www.corvellamarine.com</text>
    </g>
    <text class="bleed-label" transform="translate(7 100) rotate(-90)" text-anchor="middle">bleed</text>
    <text class="bleed-label" x="96" y="161">bleed</text>
  </g>

  <!-- Back, blue field -->
  <g class="card-back on-blue" transform="translate(293 295)">
    <rect class="bleed-area" width="273" height="163"/>
    <g transform="translate(9 9)">
      <g clip-path="url(#card-shape)">
        <rect width="252" height="147" fill="var(--brand-blue)"/>
        <rect y="123" width="252" height="24" fill="var(--brand-orange)"/>
      </g>
      <text class="holder-name" x="13" y="23">DALE PRITCHETT</text>
      <text class="holder-title" x="13" y="32">CORPORATE MANAGER</text>
      <use class="contact-icon" href="#icon-phone" x="125" y="40"/>
      <text class="contact-line" x="135" y="39">1.954.382.7146</text>
      <text class="contact-line" x="135" y="46">1.954.451.8320</text>
      <use class="contact-icon" href="#icon-fax" x="125" y="61"/>
      <text class="contact-line" x="135" y="63">1.954.382.7139</text>
      <use class="contact-icon" href="#icon-home" x="125" y="79"/>
      <text class="contact-line" x="135" y="78">718 West Halden Lane</text>
      <text class="contact-line" x="135" y="86">Marlow Harbor, FL 33019</text>
      <use class="contact-icon" href="#icon-mail" x="125" y="99"/>
      <text class="contact-line" x="135" y="101">212@corvellamarine.com</text>
      <rect class="social-square" x="14" y="94" width="10" height="10" rx="1"/>
      <rect class="social-square" x="29" y="94" width="10" height="10" rx="1"/>
      <rect class="social-square" x="44" y="94" width="10" height="10" rx="1"/>
      <text class="web-address" x="126" y="138" text-anchor="middle">www.corvellamarine.com</text>
    </g>
    <text class="bleed-label" transform="translate(6 100) rotate(-90)" text-anchor="middle">bleed</text>
    <text class="bleed-label" x="95" y="161">bleed</text>
  </g>

  <!-- Brand colour swatches -->
  <g class="colour-swatches">
    <rect x="486" y="556" width="30" height="20" fill="var(--brand-blue)"/>
    <rect x="516" y="556" width="30" height="20" fill="var(--brand-orange)"/>
  </g>
</svg>
</body>
</html>
```